Silverleaf Rise Accounting Program

size of ad Full: 7” x 9.6”
1- this is for a ladies program so it should appeal to women.
2-however, I do not want any pictures of people in this ad.
3-all the text should be seen and not covered over by graphics.
4-It should be an ad that will draw people's attention and people should look at it and say it looks nice I want to see that ad.
5-I have put all the instructions in yellow in the file below.
6-please leave 1 inch for the footer .
good luck with this project

• no picture or vector of people.

```html
<!DOCTYPE html>
<html lang="en">
<head>
<meta charset="utf-8">
<title>Silverleaf Rise Accounting Program – Open House</title>
<link rel="stylesheet" href="https://fonts.googleapis.com/css2?family=Bebas+Neue&family=Montserrat:wght@400;500;600;700;800;900&display=swap">
<style>
  :root {
    --purple: #7952a8;
    --magenta: #cf0a58;
    --cream: #f5ef9c;
    --sky: #a9c8f0;
    --salmon: #f59e8f;
    --white: #ffffff;
    --paper: #fbfbfb;
    --navy: #1f3560;
    --tick: #12a6e3;
    --blue: #0aa8e6;
    --band: #e9e9e9;
    --ink: #222222;
    --muted: #555555;
    --orange: #e57b1d;
    --red: #d70b0b;
  }
  * { margin: 0; padding: 0; box-sizing: border-box; }
  html, body { width: 938px; height: 1200px; overflow: hidden; background: var(--paper); }
  .flyer { display: block; width: 938px; height: 1200px; }
  .headline { font-family: "Bebas Neue", "Oswald", sans-serif; }
  .body-type { font-family: "Montserrat", "Helvetica Neue", Arial, sans-serif; }
</style>
</head>
<body>
<svg class="flyer" viewBox="0 0 938 1200" width="938" height="1200" xmlns="http://www.w3.org/2000/svg">
  <defs>
    <linearGradient id="lettering-fill" x1="0" y1="0" x2="1" y2="1">
      <stop offset="0" stop-color="#f6e3ea"/>
      <stop offset="1" stop-color="#ececec"/>
    </linearGradient>
  </defs>

  <!-- page -->
  <rect class="page" x="0" y="0" width="938" height="1200" fill="var(--paper)"/>

  <!-- attention band -->
  <rect class="attention-band" x="0" y="0" width="938" height="86" fill="var(--purple)"/>
  <text class="attention-title body-type" x="469" y="63" text-anchor="middle" font-size="52" font-weight="800" fill="var(--white)" textLength="840" lengthAdjust="spacing">ATTENTION WOMEN</text>

  <!-- hero -->
  <path class="hero-panel" d="M0 86 H938 V499 Q469 660 0 499 Z" fill="var(--magenta)"/>
  <text class="hero-kicker headline" x="469" y="193" text-anchor="middle" font-size="118" fill="var(--white)" textLength="745" lengthAdjust="spacingAndGlyphs">A MASTER’S DEGREE IN</text>
  <text class="hero-title headline" x="467" y="350" text-anchor="middle" font-size="200" fill="var(--cream)" textLength="750" lengthAdjust="spacingAndGlyphs">ACCOUNTING</text>
  <text class="hero-line body-type" x="469" y="404" text-anchor="middle" font-size="32" font-weight="700" fill="var(--white)" textLength="541" lengthAdjust="spacingAndGlyphs">A STABLE, LUCRATIVE CAREER, WITH</text>
  <text class="hero-line hero-line--accent body-type" x="469" y="450" text-anchor="middle" font-size="42" font-weight="800" fill="var(--sky)" textLength="700" lengthAdjust="spacingAndGlyphs">HIGH-PAYING, FULL / PART TIME</text>
  <text class="hero-line body-type" x="469" y="492" text-anchor="middle" font-size="33" font-weight="800" fill="var(--white)" textLength="328" lengthAdjust="spacingAndGlyphs">OPPORTUNITIES IN</text>
  <text class="hero-line hero-line--sector body-type" x="469" y="534" text-anchor="middle" font-size="33" font-weight="700" fill="var(--salmon)" textLength="520" lengthAdjust="spacingAndGlyphs">PRIVATE / PUBLIC COMPANIES</text>

  <!-- placement advantage -->
  <rect class="placement-lettering" x="48" y="603" width="359" height="204" rx="6" fill="url(#lettering-fill)" role="img" aria-label="Hand lettering: The Kestrel Job Placement Advantage"/>
  <line class="placement-divider" x1="463" y1="616" x2="463" y2="782" stroke="var(--ink)" stroke-width="2"/>

  <g class="placement-points body-type" fill="var(--navy)" font-size="25" font-weight="500">
    <g class="tick">
      <circle cx="521" cy="637" r="12" fill="none" stroke="var(--tick)" stroke-width="2"/>
      <path d="M515 637 l4.5 4.5 l8 -8.5" fill="none" stroke="var(--tick)" stroke-width="2.4" stroke-linecap="round" stroke-linejoin="round"/>
    </g>
    <text x="557" y="646" textLength="276" lengthAdjust="spacingAndGlyphs">96% Placement Rate</text>
    <g class="tick">
      <circle cx="521" cy="683" r="12" fill="none" stroke="var(--tick)" stroke-width="2"/>
      <path d="M515 683 l4.5 4.5 l8 -8.5" fill="none" stroke="var(--tick)" stroke-width="2.4" stroke-linecap="round" stroke-linejoin="round"/>
    </g>
    <text x="557" y="692" textLength="293" lengthAdjust="spacingAndGlyphs">6 placement directors</text>
    <g class="tick">
      <circle cx="521" cy="731" r="12" fill="none" stroke="var(--tick)" stroke-width="2"/>
      <path d="M515 731 l4.5 4.5 l8 -8.5" fill="none" stroke="var(--tick)" stroke-width="2.4" stroke-linecap="round" stroke-linejoin="round"/>
    </g>
    <text x="557" y="740" textLength="333" lengthAdjust="spacingAndGlyphs">Decades of relationships</text>
    <text x="557" y="768" textLength="243" lengthAdjust="spacingAndGlyphs">with 100’s of firms</text>
  </g>

  <!-- open house band -->
  <rect class="event-band" x="0" y="832" width="938" height="115" fill="var(--band)"/>
  <path class="event-badge" d="M41 832 H195 V926 Q195 942 179 942 H57 Q41 942 41 926 Z" fill="var(--blue)"/>
  <g class="event-badge-text body-type" fill="var(--white)" font-weight="800" text-anchor="middle">
    <rect x="56" y="846" width="18" height="14" rx="2"/>
    <text x="132" y="860" font-size="21" textLength="108" lengthAdjust="spacingAndGlyphs">MEETLY</text>
    <text x="118" y="899" font-size="38" textLength="152" lengthAdjust="spacingAndGlyphs">OPEN</text>
    <text x="118" y="930" font-size="30" textLength="150" lengthAdjust="spacingAndGlyphs">HOUSE</text>
  </g>

  <text class="event-date body-type" x="233" y="890" font-size="73" font-weight="900" fill="var(--blue)" textLength="331" lengthAdjust="spacingAndGlyphs">JUNE 14</text>
  <text class="event-time body-type" x="233" y="932" font-size="21" font-weight="600" fill="var(--muted)" textLength="329" lengthAdjust="spacing">SUNDAY @2PM</text>

  <line class="event-divider" x1="596" y1="851" x2="596" y2="933" stroke="#888" stroke-width="1.5"/>

  <g class="event-contact body-type" text-anchor="middle">
    <text x="760" y="869" font-size="13.5" fill="var(--muted)">For a Meetly link / conference</text>
    <text x="760" y="888" font-size="13.5" fill="var(--muted)">number /information</text>
    <text x="727" y="914" font-size="17" font-weight="700" fill="var(--blue)" textLength="194" lengthAdjust="spacingAndGlyphs">INFO@KESTRELJOBS.ORG</text>
    <text x="850" y="914" font-size="17" font-weight="700" fill="var(--ink)">OR</text>
    <text x="764" y="937" font-size="17" font-weight="700" fill="var(--blue)" textLength="166" lengthAdjust="spacingAndGlyphs">555 014 2200 X 111</text>
  </g>

  <!-- footer -->
  <circle class="ranking-badge" cx="72" cy="1010" r="28" fill="var(--orange)" opacity="0.85"/>

  <g class="university body-type" text-anchor="middle">
    <text x="417" y="993" font-size="25" font-weight="800" fill="var(--orange)" textLength="494" lengthAdjust="spacingAndGlyphs">HARROWGATE RIDGE UNIVERSITY</text>
    <text x="417" y="1011" font-size="14" font-weight="600" fill="var(--ink)">Masters in Accounting program</text>
    <text x="417" y="1028" font-size="11.5" font-weight="600" fill="var(--ink)">Received the highest possible rating in USA</text>
  </g>

  <path class="url-bar" d="M146 1034 H685 L675 1060 H146 Z" fill="var(--blue)"/>
  <g class="url-icon" fill="none" stroke="var(--white)" stroke-width="1.3">
    <circle cx="161" cy="1047" r="8"/>
    <ellipse cx="161" cy="1047" rx="3.5" ry="8"/>
    <line x1="153" y1="1047" x2="169" y2="1047"/>
  </g>
  <text class="url-text body-type" x="178" y="1053" font-size="16" font-weight="700" fill="var(--white)" textLength="450" lengthAdjust="spacingAndGlyphs">HTTPS://KESTRELJOBS.ORG/OPEN-HOUSE</text>

  <path class="duration-tag" d="M703 961 H938 V1051 H670 Z" fill="var(--red)"/>
  <g class="duration-text body-type" fill="var(--white)" font-weight="800" text-anchor="middle">
    <text x="808" y="1011" font-size="25" textLength="164" lengthAdjust="spacingAndGlyphs">MASTERS IN</text>
    <text x="808" y="1040" font-size="31" textLength="206" lengthAdjust="spacingAndGlyphs">12 MONTHS</text>
  </g>
</svg>
</body>
</html>
```